Harlow Capital - Financial Planning Solutions

Harlow Capital is a financial planning business in Melbourne, Australia. We cater to all kinds of clients from high net worth individuals to young people just starting a career. We need a chart, which will be included in client pitches, presentations and on our website, that conveys the various areas that we are able to provide client solutions.
We have attached three rudimentary interpretations of what we're talking about, one of which includes our logo. With each area of advice we have included a brief description of what it is. The different areas are not necessarily linked, so it's not a circular process but there is a logical progression to them: clients can ask us to get involved with any of the steps.
We are pretty open to suggestions as to the best presentation but are quite interested in an infographics approach.
You can check out our website at www.harlowcapital.com.au to see a bit about us, but please be aware that we are changing our investment philosophy and the tone of the website to a broader appeal.
Cheers, Oliver

Industry/Entity Type

Investment

```html
<!DOCTYPE html>
<html lang="en">
<head>
<meta charset="utf-8">
<title>Harlow Capital – Areas of Advice</title>
<link rel="stylesheet" href="https://fonts.googleapis.com/css2?family=Tinos&family=Josefin+Sans:wght@400&display=swap">
<style>
  :root {
    --bg-warm: #e4dfcb;
    --bg-light: #fbfaf6;
    --frame: #0d0d0d;
    --panel-warm: #ece8d9;
    --panel-light: #fdfdfb;
    --box-core: #e2ddc8;
    --box-edge: #c3ba9c;
    --ink: #111111;
    --brand-ink: #1c1c1c;
  }
  * { margin: 0; padding: 0; box-sizing: border-box; }
  html, body { width: 1200px; height: 900px; overflow: hidden; }
  body {
    position: relative;
    background: linear-gradient(90deg, var(--bg-warm) 0%, var(--bg-light) 100%);
    font-family: "Tinos", "Times New Roman", serif;
    color: var(--ink);
  }
  .frame {
    position: absolute;
    left: 26px; top: 35px; width: 1142px; height: 835px;
    background: var(--frame);
  }
  .panel {
    position: absolute;
    left: 55px; top: 61px; width: 1082px; height: 783px;
    background: linear-gradient(90deg, var(--panel-warm) 0%, var(--panel-light) 100%);
  }
  .brand-gap {
    position: absolute;
    left: 536px; top: 35px; width: 123px; height: 26px;
    background: linear-gradient(90deg, #f1eee4, #f3f1e9);
  }
  .brand {
    position: absolute;
    left: 450px; top: 37px; width: 300px;
    text-align: center;
    font-family: "Josefin Sans", "Helvetica Neue", sans-serif;
    font-weight: 400;
    color: var(--brand-ink);
  }
  .brand-mark {
    display: block;
    width: 30px; height: 30px;
    margin: 0 auto 8px;
    background: var(--brand-ink);
  }
  .brand-name { font-size: 28px; letter-spacing: 4px; line-height: 1; }
  .brand-sub { font-size: 15px; letter-spacing: 5px; line-height: 1; margin-top: 6px; }
  .service {
    position: absolute;
    height: 74px;
    display: flex; align-items: center; justify-content: center;
    text-align: center;
    font-size: 17px; line-height: 1.3;
    text-transform: uppercase;
    background: radial-gradient(ellipse at center, var(--box-core) 0%, var(--box-edge) 100%);
  }
  .note {
    position: absolute;
    font-size: 18.5px;
    white-space: nowrap;
    line-height: 1;
  }
  .note--right { text-align: right; }
</style>
</head>
<body>
  <div class="frame"></div>
  <div class="panel"></div>
  <div class="brand-gap"></div>

  <header class="brand">
    <span class="brand-mark"></span>
    <div class="brand-name">HARLOW</div>
    <div class="brand-sub">CAPITAL</div>
  </header>

  <main class="services">
    <div class="service" style="left:96px; top:111px; width:172px;">Income<br>Gengeration</div>

    <div class="service" style="left:206px; top:211px; width:173px;">Tax<br>Advice</div>
    <p class="note" style="left:393px; top:242px;">To maximize after tax income</p>

    <div class="service" style="left:316px; top:319px; width:172px;">Financial<br>Planning</div>
    <p class="note" style="left:502px; top:350px;">A road map for application of your after tax income</p>

    <div class="service" style="left:449px; top:431px; width:172px;">Debt</div>
    <p class="note" style="left:634px; top:460px;">To fund the purchase of a house or other asset</p>

    <div class="service" style="left:598px; top:536px; width:193px;">Superannuation</div>
    <p class="note note--right" style="right:614px; top:566px;">Potentially your largest or second largest asset</p>

    <div class="service" style="left:764px; top:635px; width:173px;">Investment<br>Portfolio</div>
    <p class="note note--right" style="right:446px; top:667px;">To optimize the return on your after tax income</p>

    <div class="service" style="left:894px; top:734px; width:210px;">Insurance/<br>Risk Protection</div>
    <p class="note note--right" style="right:318px; top:764px;">Protect the lifestyle you’ve built for you and your family</p>
  </main>
</body>
</html>
```